Modern Innovative Business Card Design

We require a nice, modern, clean business card design, ready for upload to Cardomora. Our company develops online banking software solutions for small financial insitutions. The design should be clean, professional, but yet not "corporate boring". See www.fyrolt.com for an idea of business image and profile. The design should communicate innovation, be modern and fresh, yet look professional and established.

Target Market(s)

Finance industry, bankers, entrepreneurs

Industry/Entity Type

Financial

Contact Information for Business Card

Tobias Wendlerup
CEO

FYROLT BV
Lindenwerf 38
1027 HX Amsterdam
The Netherlands

Phone: +31 20 517 8036
Direct: +31 20 604 1758
Skype: tobias.fyrolt
ceo@fyrolt.com
www.fyrolt.com

Font styles to use
Sans Serif

Requirements
Must have
• Should look clean, modern and professional. File should be ready for upload to cardomora.
Should not have
• Boring standard corporate layout

```html
<!DOCTYPE html>
<html lang="en">
<head>
<meta charset="utf-8">
<title>FYROLT BV – Business Card</title>
<link rel="stylesheet" href="https://fonts.googleapis.com/css2?family=Mulish:wght@300;400;600;800&family=PT+Sans&display=swap">
<style>
  :root {
    --backdrop: #7a4c1f;
    --card: #ffffff;
    --lime: #94c541;
    --graphite: #55575a;
    --ink: #2b2b2b;
    --rule: #6e6e6e;
  }
  html, body {
    margin: 0;
    padding: 0;
    width: 1200px;
    height: 1000px;
    overflow: hidden;
    background: var(--backdrop);
  }
  .canvas {
    position: relative;
    width: 1200px;
    height: 1000px;
  }
  .business-card {
    position: absolute;
    left: 145px;
    top: 240px;
    width: 910px;
    height: 520px;
    background: var(--card);
    overflow: hidden;
    box-shadow: 0 2px 6px rgba(0,0,0,0.25);
  }
  .wave-band {
    position: absolute;
    left: 59px;
    top: 0;
    width: 318px;
    height: 115px;
  }
  .brand-name {
    position: absolute;
    left: 57px;
    top: 148px;
    margin: 0;
    font-family: "Mulish", sans-serif;
    font-weight: 800;
    font-size: 86px;
    line-height: 1;
    letter-spacing: 4px;
    color: var(--graphite);
  }
  .accent-block {
    position: absolute;
    left: 59px;
    top: 288px;
    width: 318px;
    height: 232px;
    background: var(--lime);
  }
  .identity {
    position: absolute;
    right: 42px;
    top: 28px;
    text-align: right;
    font-family: "Mulish", sans-serif;
  }
  .person-name {
    margin: 0;
    font-weight: 300;
    font-size: 40px;
    line-height: 48px;
    color: var(--lime);
  }
  .person-title {
    margin: 4px 0 0;
    font-weight: 600;
    font-size: 24px;
    letter-spacing: 1.5px;
    line-height: 30px;
    color: var(--graphite);
  }
  .divider {
    position: absolute;
    left: 447px;
    right: 0;
    top: 290px;
    height: 0;
    border-top: 1.5px solid var(--rule);
  }
  .contact {
    position: absolute;
    right: 42px;
    top: 306px;
    margin: 0;
    text-align: right;
    font-family: "PT Sans", sans-serif;
    font-style: normal;
    font-size: 21px;
    line-height: 27.6px;
    color: var(--ink);
  }
  .contact span { display: block; }
  .contact .web { color: var(--lime); }
</style>
</head>
<body>
<main class="canvas">
  <section class="business-card" aria-label="FYROLT BV business card">
    <svg class="wave-band" viewBox="0 0 318 115" aria-hidden="true">
      <path d="M0 0 H318 V62 C250 70 200 95 150 108 C95 120 35 110 0 72 Z" fill="var(--lime)"/>
    </svg>

    <h1 class="brand-name">FYROLT</h1>

    <div class="accent-block" aria-hidden="true"></div>

    <header class="identity">
      <p class="person-name">Tobias Wendlerup</p>
      <p class="person-title">CEO FYROLT BV</p>
    </header>

    <div class="divider" aria-hidden="true"></div>

    <address class="contact">
      <span>Lindenwerf 38</span>
      <span>1027 HX Amsterdam</span>
      <span>The Netherlands</span>
      <span>Phone: +31 20 517 8036</span>
      <span>Direct: +31 20 604 1758</span>
      <span>Skype: tobias.fyrolt ceo@fyrolt.com</span>
      <span class="web">www.fyrolt.com</span>
    </address>
  </section>
</main>
</body>
</html>
```